BRIGHTDESK - Remote Tech Support Site

We are looking for a new very responsive and simple website for our brand Brightdesk.example - a remote technical support company.

This company supports customers Globally in different countries throughout Eur/ North America / South America / Asia etc (please keep this in mind and integrate into the idea).

Its important to us that the design is very explanatory, the customer should easily be able to figure out that we provide computer support right away ... I like one page responsive type designs as well without a bunch of menu items

Here are some similar sites we like - but still looking for a unique design that fits out brand "brightdesk" - I have upload also some layouts i like (but the designs are not important just the layouts), youll see it includes consumer business etc which is important.

PLOVE.EXAMPLE - I love how clean it is - nice and white easy to see everything

ZENBYTE247.EXAMPLE - also nice the layout and responsive one page design makes it easy to use

lumacorefix.example - similar to zenbyte design as well - you can get the idea im looking for between the two

You will notice those examples are much different then the attachments I added - again this is more of an idea for possible layouts .. attached is also the logo - could inspire color scheme / blue white black etc

Target Market(s)

Home consumers without computer knowledge , older age 45-65, small medium business ... computer repair - slow computers

Industry/Entity Type

Computer Repair

Logo Text

Brightdesk

Coding

Coded - Design and coding required

Number of Pages Required

1 page

Font styles to use
Sans Serif
Other font styles liked:
• your choice responsive

Colors

Designer to choose colors to be used in the design.

Requirements
Must have
• Clean - responsive - professional design - the name says it all - brightdesk
• CALL TO ACTIONS FOR "Get Help Now!" / "Learn More" etc
Nice to have
• We are looking for a new very responsive and simple website for our brand Brightdesk.example - a remote technical support company.
• This company supports customers Globally in different countries throughout Eur/ North America / South America / Asia etc (please keep this in mind and integrate into the idea).
• Its important to us that the design is very explanatory, the customer should easily be able to figure out that we provide computer support right away ... I like one page responsive type designs as well without a bunch of menu items
• Here are some similar sites we like - but still looking for a unique design that fits out brand "brightdesk" - I have upload also some layouts i like (but the designs are not important just the layouts), youll see it includes consumer business etc which is important.
• PLOVE.EXAMPLE - I love how clean it is - nice and white easy to see everything
• ZENBYTE247.EXAMPLE - also nice the layout and responsive one page design makes it easy to use
• lumacorefix.example - similar to zenbyte design as well - you can get the idea im looking for between the two
Should not have
• dark, packed page - bad small font -

```html
<!DOCTYPE html>
<html lang="en">
<head>
<meta charset="utf-8">
<title>Brightdesk – Remote Tech Support</title>
<link href="https://fonts.googleapis.com/css2?family=Lato:wght@300;400;700;900&display=swap" rel="stylesheet">
<style>
:root{
  --blue:#2d8ff0;
  --blue-deep:#1f7ae0;
  --blue-soft:#5aa8f5;
  --black:#000;
  --ink:#1c1c1c;
  --dark:#0b0d10;
  --white:#fff;
  --grey:#6b6b6b;
  --line:#d9d9d9;
}
*{box-sizing:border-box;margin:0;padding:0}
html,body{width:1200px;height:4225px;overflow:hidden}
body{font-family:'Lato',Arial,sans-serif;color:var(--ink);background:var(--white);position:relative}
section,header,footer{position:relative;width:1200px;overflow:hidden}
.btn{display:inline-flex;align-items:center;justify-content:center;gap:8px;border-radius:30px;font-weight:700;font-size:17px;letter-spacing:.5px;text-transform:uppercase;text-decoration:none}
.btn-blue{background:var(--blue);color:var(--white)}
.btn-black{background:var(--black);color:var(--white)}
.btn-outline{border:2px solid rgba(255,255,255,.6);background:rgba(255,255,255,.15);color:var(--white)}
.accent{color:var(--blue)}

/* top bar */
.topbar{position:relative;height:40px;background:var(--black)}
.search{position:absolute;left:80px;top:8px;width:210px;height:24px;background:var(--white);border:1px solid var(--blue);font-size:14px;line-height:16px;color:var(--grey);padding:3px 8px}
.search-btn{position:absolute;left:290px;top:8px;width:24px;height:24px;background:var(--white)}
.account{position:absolute;left:780px;top:10px;color:var(--white);font-size:16px;line-height:20px;display:flex;gap:40px}
.lang{position:absolute;left:1018px;top:4px;width:104px;height:32px;background:var(--white);font-size:15px;line-height:18px;padding:7px 14px;color:var(--ink)}
/* nav */
.nav{position:relative;height:84px;background:var(--black);border-top:1px solid #222}
.brand{position:absolute;left:80px;top:18px;display:flex;align-items:center;gap:12px}
.brand-dot{width:46px;height:46px;border-radius:50%;background:var(--blue)}
.brand-name{font-size:40px;line-height:46px;font-weight:700;color:var(--white);letter-spacing:-.5px}
.menu{position:absolute;left:442px;top:30px;display:flex;gap:37px;font-size:16px;line-height:20px;font-weight:700;color:var(--white)}
.menu .active{border-bottom:3px solid var(--blue);padding-bottom:31px}

/* hero */
.hero{height:575px;background:linear-gradient(180deg,#eceef1 0%,#d9dde2 70%,#c9ccd1 100%)}
.hero-photo{position:absolute;left:80px;top:0;width:420px;height:575px;background:radial-gradient(ellipse at 50% 55%,#4b6d93 0%,#8ea2b8 45%,rgba(217,221,226,0) 75%)}
.hero-title{position:absolute;left:634px;top:50px;font-size:52px;line-height:62px;font-weight:900;color:var(--white);text-shadow:0 2px 6px rgba(0,0,0,.35)}
.hero-list{position:absolute;left:632px;top:205px;list-style:none;font-size:22px;line-height:31px;color:var(--ink)}
.hero-list li::before{content:"";display:inline-block;width:8px;height:8px;border-radius:50%;background:var(--ink);margin-right:14px;vertical-align:middle}
.hero-list li.plain::before{visibility:hidden}
.hero .btn{position:absolute;left:631px;top:410px;width:186px;height:52px}

/* about */
.about{height:343px;background:linear-gradient(90deg,var(--blue-deep),var(--blue-soft) 50%,var(--blue-deep));text-align:center;color:var(--white)}
.about h2{font-size:40px;font-weight:400;padding-top:42px;letter-spacing:1px}
.about p{font-size:16px;line-height:26px;width:1060px;margin:18px auto 0}
.about .btn{position:absolute;left:494px;top:250px;width:174px;height:50px}

/* how it works */
.how{height:513px;background:var(--black);color:var(--white);text-align:center}
.how h2{font-size:40px;font-weight:400;padding-top:48px}
.steps{display:flex;justify-content:center;gap:60px;margin-top:40px}
.step{width:320px}
.step-icon{width:124px;height:124px;border-radius:50%;background:var(--white);margin:0 auto;display:flex;align-items:center;justify-content:center}
.step h3{color:var(--blue);font-size:22px;font-weight:700;margin-top:20px}
.step p{font-size:15px;line-height:23px;margin-top:10px}
.how .btn{position:absolute;left:512px;top:410px;width:172px;height:50px}

/* stats */
.stats{height:192px;display:flex;justify-content:center;text-align:center}
.stat{width:264px;padding-top:28px}
.stat b{display:block;font-size:40px;font-weight:700;margin-top:8px}
.stat span{font-size:16px;color:var(--grey)}

/* real-time */
.realtime{height:464px;background:linear-gradient(90deg,var(--blue-deep),var(--blue) 60%,#5eb0f7);color:var(--white)}
.realtime h2{position:absolute;left:80px;top:50px;font-size:40px;font-weight:400;line-height:46px}
.features{position:absolute;left:80px;top:175px;list-style:none;font-size:20px;line-height:42px}
.features li{display:flex;align-items:center;gap:12px}
.realtime .btn{position:absolute;left:80px;top:350px;width:244px;height:50px}
.monitor{position:absolute;left:652px;top:50px;width:470px;height:330px}
.screen{position:absolute;left:0;top:0;width:470px;height:290px;background:#111;border-radius:10px;padding:12px}
.screen-img{width:100%;height:100%;background:linear-gradient(135deg,#5a4738,#9a7456 45%,#3d4b55)}
.stand{position:absolute;left:195px;top:290px;width:80px;height:32px;background:#c8ccd2}
.base{position:absolute;left:160px;top:320px;width:150px;height:8px;background:#b4b8be;border-radius:4px}

/* member */
.member{height:178px;background:var(--white)}
.member h2{position:absolute;left:80px;top:48px;font-size:40px;font-weight:400;line-height:44px;color:var(--ink)}
.member .from{position:absolute;left:528px;top:78px;font-size:18px;color:var(--grey)}
.price-badge{position:absolute;left:704px;top:38px;width:110px;height:110px;border-radius:50%;border:8px solid var(--blue);display:flex;flex-direction:column;align-items:center;justify-content:center}
.price-badge b{font-size:26px;font-weight:700}
.price-badge span{font-size:13px}
.member .btn{position:absolute;left:937px;top:68px;width:186px;height:50px}

/* best features */
.best{height:743px;background:linear-gradient(180deg,#0e1013,#1a2128 50%,#0b0d10);color:var(--white);text-align:center}
.best h2{font-size:40px;font-weight:400;padding-top:48px}
.grid{display:grid;grid-template-columns:repeat(4,240px);column-gap:26px;row-gap:50px;justify-content:center;margin-top:44px}
.feature .ico{width:124px;height:124px;border-radius:50%;background:var(--blue);margin:0 auto;display:flex;align-items:center;justify-content:center}
.feature h3{color:var(--blue);font-size:20px;font-weight:400;margin-top:20px}
.feature p{font-size:15px;line-height:22px;margin-top:8px}

/* pricing */
.pricing{height:592px;text-align:center}
.pricing h2{font-size:40px;font-weight:400;padding-top:56px}
.plans{display:flex;justify-content:center;gap:60px;margin-top:50px}
.plan{width:302px;height:370px;border:1px solid var(--line);border-radius:8px;padding-top:30px;box-shadow:0 2px 6px rgba(0,0,0,.08)}
.plan h3{font-size:19px;font-weight:400}
.plan .cost{color:var(--blue);font-size:40px;font-weight:700;margin-top:14px}
.plan .cost small{font-size:16px;font-weight:400}
.plan .setup{color:var(--blue);font-size:15px;padding-bottom:18px;border-bottom:1px solid var(--line);margin:6px 26px 0}
.plan p{font-size:15px;line-height:23px;color:var(--grey);margin-top:22px;height:80px}
.plan .btn{width:184px;height:50px;margin-top:12px}

/* call */
.call{height:346px;background:var(--blue);color:var(--white)}
.call h2{position:absolute;left:80px;top:52px;font-size:40px;font-weight:400;line-height:44px}
.call p{position:absolute;left:80px;top:184px;font-size:23px;line-height:38px}
.call .hl{color:#0a2c55}
.call small{position:absolute;left:80px;top:268px;font-size:20px}
.tech-photo{position:absolute;left:900px;top:20px;width:230px;height:326px;background:linear-gradient(160deg,#4a7fb8,#1d3c63 70%,#132a47)}

/* footer */
.footer{height:155px;background:var(--black);color:var(--white);text-align:center;overflow:visible}
.to-top{position:absolute;left:580px;top:-20px;width:40px;height:40px;background:var(--white);transform:rotate(45deg);display:flex;align-items:center;justify-content:center}
.to-top svg{transform:rotate(-45deg)}
.footer .brand{position:static;justify-content:center;padding-top:40px}
.footer .brand-dot{width:40px;height:40px}
.footer .brand-name{font-size:36px;line-height:40px}
.footer .copy{font-size:14px;margin-top:14px}
</style>
</head>
<body>

<header>
  <div class="topbar">
    <div class="search">Search here...</div>
    <div class="search-btn"></div>
    <div class="account"><span>Register</span><span>Login</span></div>
    <div class="lang">ENG ▾</div>
  </div>
  <nav class="nav">
    <div class="brand"><span class="brand-dot"></span><span class="brand-name">brightdesk</span></div>
    <div class="menu">
      <span class="active">Home</span><span>About</span><span>Online Support</span><span>Services</span><span>Faqs</span><span>Pricing</span><span>Blog</span><span>Contact</span>
    </div>
  </nav>
</header>

<section class="hero">
  <div class="hero-photo" role="img" aria-label="Smiling woman sitting cross-legged with a laptop"></div>
  <h1 class="hero-title">Dedicated Support<br>Anytime. Anywhere.</h1>
  <ul class="hero-list">
    <li>Instant Support</li>
    <li>Real-Time Optimization</li>
    <li>Free Diagnostic</li>
    <li>Quick Setup &amp; Install</li>
    <li>Leading Security Software</li>
    <li class="plain">Unlimited Cloud Backup</li>
  </ul>
  <a class="btn btn-blue">Get Help Now!</a>
</section>

<section class="about">
  <h2>ABOUT</h2>
  <p>Our team is a leader in providing top notch quality services and products with a focus on our customer's needs. We are happy to discuss your computer issues and provide a free valuable diagnostic to determine the best solutions.</p>
  <p>While you are looking for the best source out there, we have everything for your computer and internet security!</p>
  <a class="btn btn-outline">Read More »</a>
</section>

<section class="how">
  <h2>HOW IT <span class="accent">WORKS</span></h2>
  <div class="steps">
    <div class="step">
      <div class="step-icon"><svg width="64" height="64" viewBox="0 0 64 64" fill="none" stroke="#000" stroke-width="4"><rect x="8" y="12" width="48" height="32" rx="3"/><path d="M4 50h56"/><path d="M22 28l8 8 12-14"/></svg></div>
      <h3>FREE Diagnostic</h3>
      <p>Get a diagnostic, FOR FREE! Get a free consultation with our staff.</p>
    </div>
    <div class="step">
      <div class="step-icon"><svg width="64" height="64" viewBox="0 0 64 64" fill="none" stroke="#000" stroke-width="5"><circle cx="32" cy="32" r="12"/><path d="M32 8v8M32 48v8M8 32h8M48 32h8M15 15l6 6M43 43l6 6M15 49l6-6M43 21l6-6"/></svg></div>
      <h3>Get Fixed</h3>
      <p>Get fixed, IMMEDIATELY! Our staff will solve your computer issues right before your eyes.</p>
    </div>
    <div class="step">
      <div class="step-icon"><svg width="64" height="64" viewBox="0 0 64 64" fill="none" stroke="#000" stroke-width="4"><ellipse cx="28" cy="14" rx="18" ry="6"/><path d="M10 14v30c0 3 8 6 18 6M46 14v14"/><path d="M10 29c0 3 8 6 18 6"/><circle cx="46" cy="46" r="12"/><path d="M46 40v6l4 3"/></svg></div>
      <h3>Backup your information!</h3>
      <p>Saving your files is now EASY! You will be able to retain your personal files without any loss of data.</p>
    </div>
  </div>
  <a class="btn btn-blue">Read More »</a>
</section>

<section class="stats">
  <div class="stat"><svg width="70" height="56" viewBox="0 0 70 56" fill="#2d8ff0"><circle cx="20" cy="14" r="10"/><circle cx="50" cy="14" r="10"/><circle cx="35" cy="20" r="11"/><path d="M2 48c0-12 8-20 18-20s18 8 18 20zM32 48c0-12 8-20 18-20s18 8 18 20z"/><path d="M14 56c0-13 9-22 21-22s21 9 21 22z"/></svg><b>25000+</b><span>Customers</span></div>
  <div class="stat"><svg width="70" height="56" viewBox="0 0 70 56" fill="#2d8ff0"><circle cx="14" cy="12" r="9"/><circle cx="35" cy="12" r="9"/><circle cx="56" cy="12" r="9"/><path d="M0 50c0-14 6-24 14-24s14 10 14 24zM21 50c0-14 6-24 14-24s14 10 14 24zM42 50c0-14 6-24 14-24s14 10 14 24z"/></svg><b>175+</b><span>Employees</span></div>
  <div class="stat"><svg width="70" height="56" viewBox="0 0 70 56"><rect x="8" y="4" width="54" height="38" rx="3" fill="#2d8ff0"/><rect x="14" y="10" width="42" height="26" fill="#fff"/><path d="M26 42h18l4 10H22z" fill="#2d8ff0"/></svg><b>65000+</b><span>Computers Repaired</span></div>
  <div class="stat"><svg width="70" height="56" viewBox="0 0 70 56"><rect x="14" y="6" width="42" height="48" rx="3" fill="#2d8ff0"/><rect x="19" y="18" width="32" height="30" fill="#fff"/><text x="35" y="40" font-family="Lato,sans-serif" font-size="16" font-weight="700" text-anchor="middle" fill="#2d8ff0">02</text></svg><b>2</b><span>Years In Business</span></div>
</section>

<section class="realtime">
  <h2>Real-Time Support Features<br>and BENEFITS</h2>
  <ul class="features">
    <li><svg width="22" height="22" viewBox="0 0 22 22" fill="none" stroke="#fff" stroke-width="2"><rect x="1" y="3" width="18" height="18"/><path d="M5 11l5 5 11-14"/></svg>24/7 Real-Time Technician Support</li>
    <li><svg width="22" height="22" viewBox="0 0 22 22" fill="none" stroke="#fff" stroke-width="2"><rect x="1" y="3" width="18" height="18"/><path d="M5 11l5 5 11-14"/></svg>The best Security Software in the market</li>
    <li><svg width="22" height="22" viewBox="0 0 22 22" fill="none" stroke="#fff" stroke-width="2"><rect x="1" y="3" width="18" height="18"/><path d="M5 11l5 5 11-14"/></svg>Regular tune-ups and optimization</li>
    <li><svg width="22" height="22" viewBox="0 0 22 22" fill="none" stroke="#fff" stroke-width="2"><rect x="1" y="3" width="18" height="18"/><path d="M5 11l5 5 11-14"/></svg>Setup and installation included</li>
  </ul>
  <a class="btn btn-black">Become a Member »</a>
  <div class="monitor">
    <div class="screen"><div class="screen-img" role="img" aria-label="Close-up of a computer circuit board on the monitor screen"></div></div>
    <div class="stand"></div><div class="base"></div>
  </div>
</section>

<section class="member">
  <h2>BECOME A<br><span class="accent">MEMBER TODAY!</span></h2>
  <span class="from">Starting At Only</span>
  <div class="price-badge"><b>$19.99</b><span>/ MONTH</span></div>
  <a class="btn btn-blue">Get Started »</a>
</section>

<section class="best">
  <h2>ALL THE BEST FEATURES, <span class="accent">AT THE BEST PRICES</span></h2>
  <div class="grid">
    <div class="feature"><div class="ico"><svg width="56" height="56" viewBox="0 0 56 56" fill="none" stroke="#fff" stroke-width="4"><path d="M28 4l20 8v14c0 14-9 22-20 26C17 48 8 40 8 26V12z"/><path d="M18 34l20-16"/></svg></div><h3>Ad Blocker</h3><p>Avoid unwanted Pop-ups with the newest Ad Blocking technology.</p></div>
    <div class="feature"><div class="ico"><svg width="56" height="56" viewBox="0 0 56 56" fill="none" stroke="#fff" stroke-width="5" stroke-linecap="round"><path d="M12 44l20-20"/><circle cx="38" cy="18" r="9"/><path d="M12 12l32 32"/></svg></div><h3>Regular Tune-Ups</h3><p>Get a Regular Tune-Up and Optimization every 90 days.</p></div>
    <div class="feature"><div class="ico"><svg width="56" height="56" viewBox="0 0 56 56" fill="none" stroke="#fff" stroke-width="4"><rect x="6" y="8" width="44" height="30" rx="2"/><path d="M20 48h16M28 38v10M28 16v12M28 32v2"/></svg></div><h3>System Reports</h3><p>Stay up to date with Real-Time System Reporting.</p></div>
    <div class="feature"><div class="ico"><svg width="56" height="56" viewBox="0 0 56 56" fill="none" stroke="#fff" stroke-width="4"><rect x="14" y="8" width="36" height="26" rx="2"/><rect x="4" y="24" width="16" height="26" rx="2"/><path d="M26 46h18M35 34v12"/></svg></div><h3>Multiple Devices</h3><p>Get support for up to 4 multiple devices. Ask about our Family Plans.</p></div>
    <div class="feature"><div class="ico"><svg width="56" height="56" viewBox="0 0 56 56" fill="#fff"><circle cx="28" cy="18" r="11"/><path d="M8 50c0-13 9-20 20-20s20 7 20 20z"/></svg></div><h3>Identity Protection</h3><p>Coming Soon.</p></div>
    <div class="feature"><div class="ico"><svg width="56" height="56" viewBox="0 0 56 56" fill="none" stroke="#fff" stroke-width="4"><rect x="16" y="4" width="24" height="48" rx="4"/><rect x="22" y="24" width="12" height="10" fill="#fff"/><path d="M24 24v-4a4 4 0 018 0v4"/></svg></div><h3>Mobile Security</h3><p>Coming Soon.</p></div>
    <div class="feature"><div class="ico"><svg width="56" height="56" viewBox="0 0 56 56" fill="none" stroke="#fff" stroke-width="4"><rect x="4" y="8" width="34" height="24" rx="2"/><rect x="24" y="20" width="28" height="22" rx="2"/><path d="M30 50h16"/></svg></div><h3>Cross Platform Support</h3><p>Coming Soon.</p></div>
    <div class="feature"><div class="ico"><svg width="56" height="56" viewBox="0 0 56 56" fill="#fff"><path d="M14 44a10 10 0 010-20 14 14 0 0127-3 11 11 0 011 23z"/><path d="M28 26l-8 8h5v8h6v-8h5z" fill="#2d8ff0"/></svg></div><h3>Cloud Backup</h3><p>Keep your data safe! Ask about our plans for Unlimited Cloud Backup.</p></div>
  </div>
</section>

<section class="pricing">
  <h2>MEMBERSHIP <span class="accent">PRICING AND PLANS</span></h2>
  <div class="plans">
    <div class="plan"><h3>PREMIUM</h3><div class="cost">$19.99 <small>/ MONTHLY</small></div><div class="setup">($249-$300 setup fee)</div><p>Regular 90-Day Optimization<br>Unlimited 24/7 Tier 3<br>Technician Support</p><a class="btn btn-black">Learn More »</a></div>
    <div class="plan"><h3>PREMIUM PLUS</h3><div class="cost">$29.99 <small>/ MONTHLY</small></div><div class="setup">($249-$300 setup fee)</div><p>Regular 90-Day Optimization<br>Unlimited 24/7 Tier 3<br>Technician Support</p><a class="btn btn-black">Learn More »</a></div>
    <div class="plan"><h3>PLATINUM</h3><div class="cost">$39.99 <small>/ MONTHLY</small></div><div class="setup">($249-$300 setup fee)</div><p>Regular 90-Day Optimization<br>Unlimited 24/7 Tier 3 Technician<br>Support Online Identity<br>Theft Protection</p><a class="btn btn-black">Learn More »</a></div>
  </div>
</section>

<section class="call">
  <h2>CALL US TODAY And get started with our<br>dedicated technicians.</h2>
  <p>Get a <span class="hl">30-minute</span> one-on-one free consultation with one of our<br>experts! *</p>
  <small>*Limited period offer</small>
  <div class="tech-photo" role="img" aria-label="Technician kneeling beside an open desktop computer tower"></div>
</section>

<footer class="footer">
  <div class="to-top"><svg width="16" height="16" viewBox="0 0 16 16" fill="none" stroke="#000" stroke-width="2.5"><path d="M3 8l5-5 5 5M3 14l5-5 5 5"/></svg></div>
  <div class="brand"><span class="brand-dot"></span><span class="brand-name">brightdesk</span></div>
  <div class="copy">© Brightdesk - 2017. All Rights Reserved.</div>
</footer>

</body>
</html>
```